Website banner

Here is the link where the current banner is featured https://www.brimlark.com.au/collections/gel-blasters

I need the banner recreated into desktop and mobile format size.
Update the key points to:
- FREE SHIPPING AUSTRALIA WIDE
- SAME DAY DISPATCH
- BEST PRICE GUARANTEE
- 3000+ 5 STAR REVIEWS
- BEST SERVICE & WARRANTY
- 100% SECURE CHECKOUT

I want the banner to suit the style of the website and make it look better than the last graphic.

I also need the "save even more" picture to be recreated as it looks very plain at the moment,

```html
<!DOCTYPE html>
<html lang="en">
<head>
<meta charset="utf-8">
<title>Gel Blasters Feature Banner and Save Even More Panel</title>
<link href="https://fonts.googleapis.com/css2?family=Rubik:wght@400;500;700;800&display=swap" rel="stylesheet">
<style>
  :root {
    --ink: #1b1b1c;
    --ink-deep: #111112;
    --red: #e01f26;
    --red-dark: #b3151b;
    --white: #ffffff;
    --stage-light: #f7f7f7;
    --stage-dark: #c4c4c4;
    --smoke: #6e6a63;
    --smoke-dark: #2a2826;
    --steel: #4b5563;
  }
  * { box-sizing: border-box; margin: 0; padding: 0; }
  html, body { width: 1200px; height: 1200px; overflow: hidden; }
  body {
    font-family: "Rubik", Arial, sans-serif;
    background: radial-gradient(ellipse at 50% 45%, var(--stage-light) 0%, #e2e2e2 45%, var(--stage-dark) 100%);
    position: relative;
  }

  .feature-banner {
    position: absolute;
    left: 14px; top: 330px;
    width: 1172px; height: 178px;
    background: var(--ink);
    overflow: hidden;
    box-shadow: 0 22px 26px -14px rgba(0,0,0,0.45);
  }
  .feature-banner__scene { position: absolute; top: 0; height: 100%; }
  .feature-banner__scene--left {
    left: 0; width: 250px;
    background:
      radial-gradient(ellipse at 28% 35%, #8a857c 0%, var(--smoke) 25%, var(--smoke-dark) 60%, transparent 85%),
      linear-gradient(90deg, #3b3936 0%, var(--ink) 100%);
  }
  .feature-banner__scene--right {
    right: 0; width: 290px;
    background:
      radial-gradient(ellipse at 75% 30%, #6f7883 0%, var(--steel) 25%, #252a30 60%, transparent 85%),
      linear-gradient(270deg, #2e333a 0%, var(--ink) 100%);
  }

  .feature-list { position: absolute; left: 212px; top: 0; display: flex; height: 100%; }
  .feature { width: 125px; height: 100%; position: relative; text-align: center; }
  .feature + .feature::before {
    content: ""; position: absolute; left: 0; top: 39px;
    width: 1.5px; height: 104px; background: var(--red);
  }
  .feature__icon {
    position: absolute; left: 50%; top: 30px;
    width: 80px; height: 80px; transform: translateX(-50%);
  }
  .feature__title {
    position: absolute; left: 0; right: 0; top: 119px;
    font-size: 11.5px; font-weight: 700; line-height: 12px;
    color: var(--white); letter-spacing: -0.1px;
  }
  .feature__title span { display: block; color: var(--red); }

  .save-panel {
    position: absolute; left: 423px; top: 600px;
    width: 236px; height: 128px;
    transform: scale(1.5); transform-origin: 0 0;
    box-shadow: 0 14px 16px -10px rgba(0,0,0,0.5);
  }
  .save-panel__body { position: absolute; left: 0; top: 7px; right: 0; bottom: 0; background: var(--ink-deep); }
  .save-panel__header {
    position: absolute; left: 18px; right: 10px; top: 0; height: 28px;
    background: var(--red);
    clip-path: polygon(0 30%, 4% 0, 96% 0, 100% 30%, 95% 100%, 5% 100%);
    display: flex; align-items: center; justify-content: center;
    color: var(--white); font-weight: 800; font-size: 17px; letter-spacing: 0.2px;
  }
  .save-panel__rows { position: absolute; left: 0; right: 0; top: 30px; }
  .tier {
    position: relative; height: 27px; margin-top: 3px;
    display: flex; align-items: center;
    border-bottom: 1px solid var(--red-dark);
  }
  .tier__order {
    width: 124px; padding-left: 14px;
    color: var(--white); font-size: 14.5px; font-weight: 400; white-space: nowrap;
  }
  .tier__discount {
    position: absolute; right: 0; top: 0; bottom: 0; width: 114px;
    background: var(--red);
    clip-path: polygon(7px 0, 100% 0, 100% 100%, 0 100%);
    display: flex; align-items: center; padding-left: 11px;
    color: var(--white); font-size: 14.5px; font-weight: 400; white-space: nowrap;
  }
  .tier__discount b { font-weight: 800; margin-left: 4px; }
</style>
</head>
<body>

<section class="feature-banner" aria-label="Store benefits banner">
  <div class="feature-banner__scene feature-banner__scene--left" role="img" aria-label="Soldier in tactical gear holding a rifle amid smoke"></div>
  <div class="feature-banner__scene feature-banner__scene--right" role="img" aria-label="Tactical team aiming rifles through smoke"></div>

  <div class="feature-list">
    <div class="feature">
      <svg class="feature__icon" viewBox="0 0 80 80" aria-hidden="true">
        <circle cx="40" cy="40" r="30" fill="none" stroke="#fff" stroke-width="4"/>
        <circle cx="40" cy="40" r="22" fill="#fff"/>
        <path d="M40 26a9 9 0 0 0-9 9c0 7 9 17 9 17s9-10 9-17a9 9 0 0 0-9-9z" fill="#1b1b1c"/>
        <circle cx="40" cy="35" r="3.5" fill="#fff"/>
      </svg>
      <div class="feature__title">FREE SHIPPING<span>AUSTRALIA WIDE</span></div>
    </div>
    <div class="feature">
      <svg class="feature__icon" viewBox="0 0 80 80" aria-hidden="true">
        <circle cx="40" cy="40" r="30" fill="none" stroke="#fff" stroke-width="4"/>
        <circle cx="40" cy="40" r="22" fill="#fff"/>
        <rect x="26" y="31" width="18" height="13" fill="#1b1b1c"/>
        <path d="M44 34h6l5 5v5H44z" fill="#1b1b1c"/>
        <circle cx="31" cy="46" r="3" fill="#1b1b1c"/>
        <circle cx="50" cy="46" r="3" fill="#1b1b1c"/>
      </svg>
      <div class="feature__title">SAME DAY<span>DISPATCH</span></div>
    </div>
    <div class="feature">
      <svg class="feature__icon" viewBox="0 0 80 80" aria-hidden="true">
        <circle cx="40" cy="40" r="30" fill="none" stroke="#fff" stroke-width="4"/>
        <circle cx="40" cy="40" r="22" fill="#fff"/>
        <circle cx="40" cy="40" r="13" fill="#1b1b1c"/>
        <text x="40" y="46" text-anchor="middle" font-family="Rubik, Arial, sans-serif" font-weight="700" font-size="17" fill="#fff">$</text>
      </svg>
      <div class="feature__title">BEST PRICE<span>GUARANTEE</span></div>
    </div>
    <div class="feature">
      <svg class="feature__icon" viewBox="0 0 80 80" aria-hidden="true">
        <circle cx="40" cy="40" r="30" fill="none" stroke="#fff" stroke-width="4"/>
        <circle cx="40" cy="40" r="22" fill="#fff"/>
        <path d="M40 26l4.1 8.8 9.6 1.1-7.1 6.6 1.9 9.5L40 47.2l-8.5 4.8 1.9-9.5-7.1-6.6 9.6-1.1z" fill="#1b1b1c"/>
      </svg>
      <div class="feature__title">3000+ 5 STAR<span>REVIEWS</span></div>
    </div>
    <div class="feature">
      <svg class="feature__icon" viewBox="0 0 80 80" aria-hidden="true">
        <circle cx="40" cy="40" r="30" fill="none" stroke="#fff" stroke-width="4"/>
        <circle cx="40" cy="40" r="22" fill="#fff"/>
        <circle cx="40" cy="40" r="13" fill="none" stroke="#1b1b1c" stroke-width="4" stroke-dasharray="4 2.8"/>
        <circle cx="40" cy="40" r="8" fill="none" stroke="#1b1b1c" stroke-width="2"/>
        <path d="M36 40l3 3 5-6" fill="none" stroke="#1b1b1c" stroke-width="2" stroke-linecap="round" stroke-linejoin="round"/>
      </svg>
      <div class="feature__title">BEST SERVICE &amp;<span>WARRANTY</span></div>
    </div>
    <div class="feature">
      <svg class="feature__icon" viewBox="0 0 80 80" aria-hidden="true">
        <circle cx="40" cy="40" r="30" fill="none" stroke="#fff" stroke-width="4"/>
        <circle cx="40" cy="40" r="22" fill="#fff"/>
        <path d="M40 26l11 4v8c0 8-5 13-11 15-6-2-11-7-11-15v-8z" fill="#1b1b1c"/>
        <circle cx="40" cy="39" r="6" fill="none" stroke="#fff" stroke-width="1.6"/>
        <path d="M37.5 39l2 2 3.5-4" fill="none" stroke="#fff" stroke-width="1.6" stroke-linecap="round" stroke-linejoin="round"/>
      </svg>
      <div class="feature__title">100% SECURE<span>CHECKOUT</span></div>
    </div>
  </div>
</section>

<section class="save-panel" aria-label="Save even more tiered discounts">
  <div class="save-panel__body"></div>
  <div class="save-panel__header">SAVE EVEN MORE</div>
  <div class="save-panel__rows">
    <div class="tier"><span class="tier__order">ORDER $250+</span><span class="tier__discount">GET <b>5% OFF</b></span></div>
    <div class="tier"><span class="tier__order">ORDER $500+</span><span class="tier__discount">GET <b>10% OFF</b></span></div>
    <div class="tier"><span class="tier__order">ORDER $1000+</span><span class="tier__discount">GET <b>15% OFF</b></span></div>
  </div>
</section>

</body>
</html>
```